'Morrow Crest' wine label

We are looking to create a new wine brand called "Morrow Crest."

We have no preconceived notions about color, design or otherwise. This design should be incorporated into a wine label that will ultimately be affixed to either a 750ml bottle or a wine box. We've attached some images of wine label artwork and bottle shots - but yours does NOT need to look like these - they're there just for illustration purposes.

Target Market(s)

Target market for this wine brand will be "broad market" retail - i.e., big box stores, wine shops, etc.

Logo Text

Morrow Crest

```html
<!DOCTYPE html>
<html lang="en">
<head>
<meta charset="utf-8">
<title>Morrow Crest — 2008 California</title>
<link rel="stylesheet" href="https://fonts.googleapis.com/css2?family=Cormorant+Garamond:wght@500;600&display=swap">
<style>
  :root {
    --plum-deep: #5e0052;
    --plum-mid: #74106f;
    --grape-red: #c21a55;
    --oval-ring-light: #d0145a;
    --oval-ring-dark: #7a0a45;
    --oval-face: #9a1a5e;
    --vintage-red: #c4144f;
    --band-dark: #2a0018;
    --band-bright: #d1155a;
    --ink-white: #ffffff;
    --frame: #000000;
  }
  * { margin: 0; padding: 0; box-sizing: border-box; }
  html, body { width: 1200px; height: 981px; overflow: hidden; background: #ffffff; }
  .label {
    position: relative;
    width: 1200px;
    height: 981px;
    overflow: hidden;
    border: 4px solid var(--frame);
    background: linear-gradient(90deg, var(--plum-deep) 0%, var(--plum-mid) 70%, var(--plum-mid) 100%);
    font-family: "Cormorant Garamond", "Times New Roman", serif;
  }
  .grape-photo {
    position: absolute;
    top: 0;
    right: 0;
    width: 400px;
    height: 100%;
    background:
      radial-gradient(ellipse 60% 22% at 70% 8%, rgba(214, 60, 120, 0.55), transparent 70%),
      radial-gradient(ellipse 55% 20% at 65% 35%, rgba(224, 40, 80, 0.6), transparent 70%),
      radial-gradient(ellipse 55% 20% at 60% 62%, rgba(200, 40, 110, 0.5), transparent 70%),
      radial-gradient(ellipse 55% 20% at 55% 88%, rgba(150, 50, 140, 0.5), transparent 70%),
      linear-gradient(90deg, rgba(116, 16, 111, 0) 0%, rgba(150, 36, 120, 0.7) 35%, var(--grape-red) 100%);
  }
  .emblem {
    position: absolute;
    left: 0;
    top: 0;
    width: 1192px;
    height: 973px;
  }
  .brand-name {
    position: absolute;
    left: 0;
    top: 0;
    width: 1192px;
    height: 973px;
    font-weight: 600;
    font-size: 150px;
    line-height: 1;
    color: var(--ink-white);
  }
  .brand-line { position: absolute; display: block; white-space: nowrap; }
  .brand-first { left: 250px; top: 215px; }
  .brand-second { left: 480px; top: 420px; }
  .vintage {
    position: absolute;
    left: 0;
    width: 1192px;
    top: 752px;
    text-align: center;
    font-size: 58px;
    font-weight: 500;
    line-height: 1;
    letter-spacing: 10px;
    color: var(--vintage-red);
  }
  .region-band {
    position: absolute;
    left: 0;
    right: 0;
    top: 834px;
    height: 62px;
    background: linear-gradient(90deg, var(--band-dark) 0%, var(--band-bright) 50%, var(--band-dark) 100%);
  }
  .region {
    position: absolute;
    left: 0;
    width: 1192px;
    top: 834px;
    height: 62px;
    line-height: 62px;
    text-align: center;
    font-size: 44px;
    font-weight: 500;
    letter-spacing: 8px;
    color: var(--ink-white);
  }
</style>
</head>
<body>
  <main class="label">
    <div class="grape-photo" role="img" aria-label="Close-up photograph of red grapes along the right edge"></div>
    <svg class="emblem" viewBox="0 0 1192 973" aria-hidden="true">
      <defs>
        <linearGradient id="ring" x1="0" y1="0" x2="1" y2="0">
          <stop offset="0" stop-color="var(--oval-ring-light)"/>
          <stop offset="1" stop-color="var(--oval-ring-dark)"/>
        </linearGradient>
      </defs>
      <ellipse cx="596" cy="395" rx="500" ry="248" fill="url(#ring)"/>
      <ellipse cx="640" cy="392" rx="450" ry="225" fill="#000000"/>
      <ellipse cx="634" cy="390" rx="446" ry="222" fill="var(--oval-face)"/>
    </svg>
    <h1 class="brand-name">
      <span class="brand-line brand-first">Morrow</span>
      <span class="brand-line brand-second">Crest</span>
    </h1>
    <p class="vintage">2008</p>
    <div class="region-band"></div>
    <p class="region">CALIFORNIA</p>
  </main>
</body>
</html>
```